Racing Simulator Website

We're a new startup designing, selling, and supporting racing simulators, specifically targeted at Track Day enthusiasts and Club Racers alike. We are differentiating ourselves from other Racing Simulator companies by fully supporting the software and hardware of our systems. The client does not need to update their software to keep the simulator running, and any issues they may run into with the hardware, we will fix. We've designed our systems with this in mind and have added features that make it as easy for the client to operate as possible. Our current website says this but doesn't do a good job of highlighting how much easier these extra features make the simulator to live with.

Our systems look like a single console in the sense that the user neither sees nor interacts with the computer underneath but just uses the simulator using a simple button box. Our computers are connected to our cloud to keep the operating system, the device drivers, and all the supported simulation games up to date, so that the system is always ready to use. Furthermore, we offer our systems as "lease-to-own" with small down payment and monthly installments, which also cover the ongoing hardware and software support for the duration of the lease. All other turnkey racing simulators require the full amount to be paid up front and do not offer software support to keep the systems up to date or provide anything beyond warranty service on the hardware.

We already have a website that contains most of this information, but it is not exciting. We're engineers building the systems but frankly do not know how to make our website exciting and compelling. We want the Home page experience to be much richer and ideally carry all these points across.

As we target track-day enthusiasts and club racers, we are positioning our simulators as tools to improve your technique and reflexes to improve your driving on the real track.
Our current website is here https://www.bluefernmotion.com
We already have more photos than what is currently on the website that you can use, or feel free to request specific photos of the system.

```html
<!DOCTYPE html>
<html lang="en">
<head>
<meta charset="utf-8">
<title>Blue Fern Motion — Racing Simulators</title>
<link href="https://fonts.googleapis.com/css2?family=Krona+One&family=Montserrat:wght@400;500;600;700&display=swap" rel="stylesheet">
<style>
:root{
  --navy:#132c45;
  --navy-deep:#0f2438;
  --gold:#d9a02a;
  --ink:#1b2a3a;
  --text:#555c66;
  --light:#efefef;
  --white:#ffffff;
}
*{box-sizing:border-box;margin:0;padding:0}
html,body{width:1200px;height:4769px;overflow:hidden}
body{position:relative;background:var(--white);font-family:'Montserrat',sans-serif;color:var(--text)}
.display{font-family:'Krona One',sans-serif;color:var(--navy);font-weight:400;letter-spacing:.3px}
.btn{position:absolute;display:flex;align-items:center;justify-content:center;background:var(--gold);color:var(--white);font-size:12px;font-weight:600}
.rule{position:absolute;height:4px;width:62px;background:var(--gold)}
.photo{position:absolute}

/* header */
.site-header{position:absolute;left:0;top:0;width:1200px;height:94px;background:var(--white)}
.brand{position:absolute;left:74px;top:30px;display:flex;align-items:center;gap:8px;font-family:'Krona One',sans-serif;font-size:24px;color:var(--navy)}
.brand .mark{width:16px;height:16px;background:var(--gold)}
.nav{position:absolute;left:360px;top:38px;display:flex;gap:22px;font-size:12px;color:#444}
.nav span.sep{color:#999}

/* hero */
.hero{position:absolute;left:0;top:94px;width:1200px;height:615px;background:linear-gradient(100deg,#e9e7e4 0%,#d9d6d2 55%,#c8c4bf 100%)}
.hero-photo{position:absolute;left:420px;top:40px;width:720px;height:560px;background:radial-gradient(ellipse at 60% 55%,#5a5856 0%,#8d8a87 45%,rgba(200,196,191,0) 72%)}
.hero h1{position:absolute;left:74px;top:152px;font-size:38px;line-height:50px;white-space:nowrap}
.hero .sub{position:absolute;left:74px;top:311px;font-family:'Krona One',sans-serif;font-size:15px;color:var(--navy)}
.hero p{position:absolute;left:74px;top:346px;width:430px;font-size:12px;line-height:19px;color:#333}
.band{position:absolute;left:0;top:709px;width:1200px;height:37px;background:var(--navy)}

/* care */
.care-photo{left:139px;top:843px;width:454px;height:457px;background:linear-gradient(160deg,#3a3a3a,#1a1a1a)}
.care h2{position:absolute;left:641px;top:866px;width:460px;font-size:24px;line-height:34px;white-space:nowrap}
.care .rule{left:641px;top:972px}
.care p{position:absolute;left:641px;top:996px;width:405px;font-size:11.5px;line-height:19px}
.feature{position:absolute;left:641px;width:405px;height:66px;display:flex;align-items:center;gap:14px;font-family:'Krona One',sans-serif;font-size:11.5px;color:var(--navy)}
.feature.lined{border-bottom:1px solid #d8d8d8}
.icon{width:44px;height:44px;background:var(--gold);display:flex;align-items:center;justify-content:center;flex:none}

/* own */
.own-title{position:absolute;left:0;width:1200px;top:1388px;text-align:center;font-size:25px}
.own .rule{left:569px;top:1428px}
.own-sub{position:absolute;left:300px;width:600px;top:1453px;text-align:center;font-size:11.5px;line-height:19px}
.ownership{position:absolute;left:117px;top:1556px;width:403px;height:153px;background:var(--navy);padding:16px 22px;color:var(--white)}
.ownership h3{font-family:'Krona One',sans-serif;font-size:12px;margin-top:10px;font-weight:400;color:var(--white)}
.ownership p{font-size:11px;line-height:16px;margin-top:5px}
.ownership .icon{width:40px;height:40px}
.own-item{position:absolute;left:117px;width:403px;height:68px;display:flex;align-items:center;gap:16px;font-family:'Krona One',sans-serif;font-size:11.5px;color:var(--navy);border-top:1px solid #d8d8d8}
.own-photo{left:632px;top:1541px;width:451px;height:454px;background:linear-gradient(170deg,#6b6e72 0%,#2b2d31 55%,#1a1b1e 100%)}

/* track */
.track{position:absolute;left:0;top:2091px;width:1200px;height:602px;background:var(--navy)}
.track h2{position:absolute;left:0;top:70px;width:1200px;text-align:center;color:var(--white);font-size:25px;line-height:34px}
.track .rule{left:569px;top:146px}
.track p{position:absolute;left:300px;top:168px;width:600px;text-align:center;color:#e4e8ee;font-size:11.5px;line-height:19px}
.track .photo{top:254px;height:268px}

/* testimonial */
.quote-mark{position:absolute;left:566px;top:2774px}
.t-title{position:absolute;left:0;width:1200px;top:2838px;text-align:center;font-size:25px}
.testimonial .rule{left:569px;top:2878px}
.t-text{position:absolute;left:245px;width:710px;top:2898px;text-align:center;font-size:13px;line-height:22px;font-style:italic;color:#555}
.t-name{position:absolute;left:0;width:1200px;top:3003px;text-align:center;font-family:'Krona One',sans-serif;font-size:11.5px;color:var(--navy)}
.dots{position:absolute;left:578px;top:3046px;display:flex;gap:8px}
.dots span{width:10px;height:10px;background:#d0d0d0}
.dots span.on{background:var(--gold)}

/* gallery */
.g-title{position:absolute;left:0;width:1200px;top:3142px;text-align:center;font-size:25px}
.gallery .rule{left:569px;top:3183px}
.plus{position:absolute;left:686px;top:3302px;width:72px;height:68px;background:var(--gold);display:flex;align-items:center;justify-content:center}

/* faq */
.f-title{position:absolute;left:0;width:1200px;top:3845px;text-align:center;font-size:25px}
.faq-item{position:absolute;left:213px;width:776px;height:44px;background:var(--light);display:flex;align-items:center;justify-content:space-between;padding:0 10px 0 30px;font-family:'Krona One',sans-serif;font-size:11.5px;color:var(--navy)}
.faq-item .toggle{width:26px;height:26px;background:var(--gold);display:flex;align-items:center;justify-content:center}

/* cta + footer */
.footer{position:absolute;left:0;top:4341px;width:1200px;height:428px;background:var(--navy)}
.cta{position:absolute;left:206px;top:4237px;width:788px;height:213px;background:var(--gold);text-align:center}
.cta h2{margin-top:44px;color:var(--white);font-size:23px}
.cta p{margin:20px auto 0;width:540px;color:var(--white);font-size:11.5px;line-height:19px}
.cta .actions{position:absolute;left:241px;top:145px;display:flex;gap:6px}
.cta .actions span{width:150px;height:38px;display:flex;align-items:center;justify-content:center;font-size:12px;font-weight:600}
.footer-brand{position:absolute;left:74px;top:4560px;display:flex;align-items:center;gap:10px;font-family:'Krona One',sans-serif;font-size:36px;color:var(--gold)}
.footer-brand .mark{width:22px;height:22px;background:var(--gold)}
.f-head{position:absolute;top:4522px;font-family:'Krona One',sans-serif;font-size:14px;color:var(--white)}
.contact-line{position:absolute;left:320px;display:flex;align-items:center;gap:10px;color:#e4e8ee;font-size:11.5px}
.contact-line .icon{width:24px;height:24px}
.news-text{position:absolute;left:597px;top:4562px;width:260px;color:#e4e8ee;font-size:11.5px;line-height:18px}
.news-field{position:absolute;left:597px;top:4610px;width:300px;height:36px;background:var(--white);display:flex;align-items:center;justify-content:space-between;padding:0 16px 0 22px;font-size:11px;color:#888}
.socials{position:absolute;left:972px;top:4558px;display:flex;gap:10px}
.socials span{width:30px;height:30px;background:var(--gold);display:flex;align-items:center;justify-content:center}
.socials span i{display:block;width:10px;height:10px;border:2px solid var(--navy)}
.f-divider{position:absolute;left:74px;top:4719px;width:1052px;height:1px;background:#3a5370}
.copyright{position:absolute;left:0;width:1200px;top:4737px;text-align:center;color:#e4e8ee;font-size:11px}
.to-top{position:absolute;left:1141px;top:4698px;width:40px;height:40px;background:var(--gold);display:flex;align-items:center;justify-content:center}
</style>
</head>
<body>

<header class="site-header">
  <div class="brand"><span class="mark"></span>BFM</div>
  <nav class="nav">
    <span>Home</span><span class="sep">|</span><span>Systems</span><span class="sep">|</span><span>Lease-to-Own</span><span class="sep">|</span><span>Support</span><span class="sep">|</span><span>About Us</span><span class="sep">|</span><span>Contact Us</span>
  </nav>
  <div class="btn" style="left:972px;top:29px;width:153px;height:38px">Book a Demo</div>
</header>

<section class="hero">
  <div class="hero-photo" role="img" aria-label="Racing simulator rig with bucket seat, wheel, pedals and triple monitors"></div>
  <h1 class="display">Experience<br>Real Track<br>Performance</h1>
  <div class="sub">Without Leaving Your Garage</div>
  <p>Engineered for serious drivers. Blue Fern Motion combines precision hardware, seamless software, and continuous cloud support — so you can focus on driving, not maintenance.</p>
  <div class="btn" style="left:74px;top:423px;width:176px;height:37px">Explore Systems</div>
</section>
<div class="band"></div>

<section class="care">
  <div class="photo care-photo" role="img" aria-label="Driver wearing a VR headset in a simulator seat"></div>
  <h2 class="display">The Only Racing<br>Simulator That Takes<br>Care of Itself</h2>
  <div class="rule"></div>
  <p>Other racing simulators need constant updates and tinkering. Ours doesn't. Blue Fern Motion handles everything — from operating system and game updates to performance optimization — automatically via the cloud.</p>
  <div class="feature lined" style="top:1080px"><span class="icon"><svg width="24" height="24" viewBox="0 0 24 24" fill="none" stroke="#fff" stroke-width="2"><path d="M19 12a7 7 0 1 1-2-5"/><path d="M17 3v4h-4"/></svg></span>Automatic Cloud Updates</div>
  <div class="feature lined" style="top:1148px"><span class="icon"><svg width="24" height="24" viewBox="0 0 24 24" fill="#fff"><rect x="3" y="8" width="18" height="9" rx="4"/><rect x="6" y="11" width="4" height="2" fill="#d9a02a"/><circle cx="16" cy="12" r="1.4" fill="#d9a02a"/></svg></span>Smart Console Design</div>
  <div class="feature" style="top:1216px"><span class="icon"><svg width="24" height="24" viewBox="0 0 24 24" fill="none" stroke="#fff" stroke-width="2"><circle cx="12" cy="12" r="8"/><path d="M10 8l5 4-5 4z" fill="#fff"/></svg></span>Reliable, Plug-and-Play Setup</div>
</section>

<section class="own">
  <h2 class="display own-title">Own the Ultimate Racing Simulator</h2>
  <div class="rule"></div>
  <p class="own-sub">Get started with a low down payment and flexible monthly installments. Your lease includes full support and automatic updates for as long as you race with us.</p>
  <div class="ownership">
    <span class="icon"><svg width="22" height="22" viewBox="0 0 24 24" fill="#fff"><circle cx="12" cy="10" r="5"/><rect x="5" y="16" width="14" height="4"/></svg></span>
    <h3>Hassle-Free Ownership</h3>
    <p>Forget about maintenance, updates, and troubleshooting. We handle everything so you can focus purely on driving and improving your lap times.</p>
  </div>
  <div class="own-item" style="top:1722px"><span class="icon"><svg width="22" height="22" viewBox="0 0 24 24" fill="none" stroke="#fff" stroke-width="2"><path d="M12 3v12M7 10l5 5 5-5M5 20h14"/></svg></span>Small Down Payment</div>
  <div class="own-item" style="top:1790px"><span class="icon"><svg width="22" height="22" viewBox="0 0 24 24" fill="none" stroke="#fff" stroke-width="2"><rect x="4" y="5" width="16" height="15"/><path d="M4 10h16M9 3v4M15 3v4"/></svg></span>Flexible Monthly Plans</div>
  <div class="own-item" style="top:1858px"><span class="icon"><svg width="22" height="22" viewBox="0 0 24 24" fill="none" stroke="#fff" stroke-width="2"><circle cx="12" cy="12" r="8"/><path d="M12 7v5l3 2"/></svg></span>Support &amp; Updates Included</div>
  <div class="btn" style="left:117px;top:1941px;width:211px;height:37px">Learn About Financing</div>
  <div class="photo own-photo" role="img" aria-label="Simulator with seat and large curved screen in a showroom"></div>
</section>

<section class="track">
  <h2 class="display">Built for Track-Day Drivers and<br>Club Racers</h2>
  <div class="rule"></div>
  <p>Every lap on our simulator sharpens your real-world reflexes and control. Our systems are trusted by drivers who want to practice smarter, save tire costs, and stay sharp between race weekends.</p>
  <div class="photo" style="left:74px;width:335px;background:linear-gradient(160deg,#b8b8b8,#5a5a5a)" role="img" aria-label="Black simulator rig with triple screens"></div>
  <div class="photo" style="left:433px;width:334px;background:linear-gradient(160deg,#9a9a9a,#444)" role="img" aria-label="Simulator seat with red accents in front of screens"></div>
  <div class="photo" style="left:791px;width:333px;background:linear-gradient(160deg,#7a8796,#2a2a2a 60%,#8a1d1d)" role="img" aria-label="Red and black simulator cockpit with monitors"></div>
</section>

<section class="testimonial">
  <svg class="quote-mark" width="68" height="46" viewBox="0 0 68 46" fill="#ecd9b3"><circle cx="16" cy="28" r="16"/><path d="M2 28 L16 0 L22 4 L12 28z"/><circle cx="50" cy="28" r="16"/><path d="M36 28 L50 0 L56 4 L46 28z"/></svg>
  <h2 class="display t-title">What Our Drivers Say</h2>
  <div class="rule"></div>
  <p class="t-text">"I used to spend hours updating and tweaking my old sim rig just to make it work with the latest game versions. Blue Fern Motion changed everything. Now I just power it on, strap in, and race. The cloud updates keep everything current, and the system feels rock-solid every time. It's like having a race engineer built into my garage."</p>
  <div class="t-name">Marcus T., Club Racer</div>
  <div class="dots"><span></span><span class="on"></span><span></span></div>
</section>

<section class="gallery">
  <h2 class="display g-title">Precision Engineering</h2>
  <div class="rule"></div>
  <div class="photo" style="left:120px;top:3224px;width:473px;height:223px;background:linear-gradient(160deg,#b08b66,#2a2420)" role="img" aria-label="Simulator in a room with acoustic panels"></div>
  <div class="photo" style="left:609px;top:3224px;width:226px;height:223px;background:linear-gradient(160deg,#4c5b6e,#1e2530)" role="img" aria-label="Cockpit view of a racing game on screen"></div>
  <div class="plus"><svg width="30" height="30" viewBox="0 0 30 30" stroke="#fff" stroke-width="2"><path d="M15 2v26M2 15h26"/></svg></div>
  <div class="photo" style="left:854px;top:3224px;width:226px;height:223px;background:linear-gradient(160deg,#c9c9c9,#3a3a3a 60%,#8a1d1d)" role="img" aria-label="Red simulator seat with monitor"></div>
  <div class="photo" style="left:120px;top:3461px;width:226px;height:225px;background:linear-gradient(160deg,#34506e,#121212 60%,#6a1616)" role="img" aria-label="Simulator in a dark room with screens"></div>
  <div class="photo" style="left:365px;top:3461px;width:226px;height:225px;background:linear-gradient(160deg,#d8d8d8,#3a3a3a)" role="img" aria-label="Simulator with racing seat and screens"></div>
  <div class="photo" style="left:609px;top:3461px;width:471px;height:225px;background:linear-gradient(160deg,#e4e4e4,#6b6b6b 60%,#2b4aa0)" role="img" aria-label="Simulator with wall-mounted accessories and blue pedals"></div>
  <div class="btn" style="left:506px;top:3724px;width:188px;height:37px">View Full Gallery</div>
</section>

<section class="faq">
  <h2 class="display f-title">Frequently Asked Questions</h2>
  <div class="faq-item" style="top:3924px">Do I need to install or update anything myself?<span class="toggle"><svg width="12" height="8" viewBox="0 0 12 8" fill="none" stroke="#fff" stroke-width="2"><path d="M1 7l5-5 5 5"/></svg></span></div>
  <div class="faq-item" style="top:3980px">What if my simulator stops working?<span class="toggle"><svg width="12" height="8" viewBox="0 0 12 8" fill="none" stroke="#fff" stroke-width="2"><path d="M1 7l5-5 5 5"/></svg></span></div>
  <div class="faq-item" style="top:4035px">Can I purchase instead of leasing?<span class="toggle"><svg width="12" height="8" viewBox="0 0 12 8" fill="none" stroke="#fff" stroke-width="2"><path d="M1 7l5-5 5 5"/></svg></span></div>
  <div class="faq-item" style="top:4091px">How fast can I start racing after setup?<span class="toggle"><svg width="12" height="8" viewBox="0 0 12 8" fill="none" stroke="#fff" stroke-width="2"><path d="M1 7l5-5 5 5"/></svg></span></div>
</section>

<footer class="footer"></footer>
<section class="cta">
  <h2 class="display" style="color:#fff">Ready to Feel the Difference?</h2>
  <p>Book a live demo and see how Blue Fern Motion transforms your practice, performance, and race preparation.</p>
  <div class="actions">
    <span style="background:var(--navy);color:#fff">Book a Demo</span>
    <span style="background:#fff;color:var(--navy)">Contact Sales</span>
  </div>
</section>

<div class="footer-brand"><span class="mark"></span>BFM</div>
<div class="f-head" style="left:320px">Contact us</div>
<div class="contact-line" style="top:4570px"><span class="icon"><svg width="12" height="12" viewBox="0 0 24 24" fill="#fff"><path d="M6 2l4 4-2 3c1 3 4 6 7 7l3-2 4 4-3 4C10 22 2 14 2 5z"/></svg></span>+1 (425) 555-0142</div>
<div class="contact-line" style="top:4606px"><span class="icon"><svg width="12" height="12" viewBox="0 0 24 24" fill="none" stroke="#fff" stroke-width="2.5"><rect x="2" y="5" width="20" height="14"/><path d="M2 5l10 8 10-8"/></svg></span>info@bluefernmotion.com</div>
<div class="f-head" style="left:597px">Newsletter</div>
<p class="news-text">Subscribe to our newsletter to receive updates on new product offerings...</p>
<div class="news-field">Enter email<svg width="16" height="16" viewBox="0 0 24 24" fill="#d9a02a"><path d="M2 12L22 3l-6 19-4-8z"/></svg></div>
<div class="f-head" style="left:972px">Social Media</div>
<div class="socials"><span><i></i></span><span><i></i></span><span><i></i></span><span><i></i></span></div>
<div class="f-divider"></div>
<div class="copyright">© 2025 Blue Fern Motion. All Rights Reserved.</div>
<div class="to-top"><svg width="12" height="8" viewBox="0 0 12 8" fill="none" stroke="#fff" stroke-width="2"><path d="M1 7l5-5 5 5"/></svg></div>

</body>
</html>
```